Business Card Design

Melodex Podcast

Industry/Entity Type

Business

Contact Information for Business Card

YOU ARE INVITED TO LISTEN
Stretch Every Idea
Award Winning Melodex Podcast
with Dr. Marla Quenby
www.drmarlaquenby-example.com

555-018-7364

```html
<!DOCTYPE html>
<html lang="en">
<head>
<meta charset="utf-8">
<title>Melodex Podcast – Business Card</title>
<link rel="stylesheet" href="https://fonts.googleapis.com/css2?family=Pinyon+Script&family=Tinos:ital@0;1&family=Questrial&display=swap">
<style>
  :root {
    --backdrop: #5b6667;
    --card-white: #ffffff;
    --brand-green: #77bc00;
    --brand-green-light: #a6d84a;
    --ink: #141414;
  }
  * { margin: 0; padding: 0; box-sizing: border-box; }
  html, body {
    width: 1200px;
    height: 1000px;
    overflow: hidden;
    background: var(--backdrop);
  }
  .card {
    position: absolute;
    left: 66px;
    top: 184px;
    width: 1079px;
    height: 634px;
    background: var(--card-white);
    box-shadow: 0 0 40px rgba(0, 0, 0, 0.35);
    overflow: hidden;
  }
  .card__panel {
    position: absolute;
    left: 0;
    top: 0;
    width: 338px;
    height: 100%;
    background: var(--brand-green);
    border-right: 3px solid var(--ink);
  }
  .card__emblem {
    position: absolute;
    left: 72px;
    top: 116px;
  }
  .card__content {
    position: absolute;
    left: 341px;
    top: 0;
    right: 0;
    height: 100%;
    color: var(--ink);
  }
  .card__line {
    position: absolute;
    left: 0;
    right: 0;
    display: flex;
    justify-content: center;
    white-space: nowrap;
    font-weight: 400;
  }
  .card__title {
    top: 30px;
    font-family: "Pinyon Script", cursive;
    font-size: 60px;
    letter-spacing: 1px;
  }
  .card__tagline {
    top: 140px;
    font-family: "Pinyon Script", cursive;
    font-size: 34px;
  }
  .card__invite {
    top: 256px;
    font-family: "Tinos", serif;
    font-size: 68px;
  }
  .card__invite span {
    display: inline-block;
    transform: scaleX(0.61);
    transform-origin: center;
  }
  .card__host {
    top: 400px;
    font-family: "Pinyon Script", cursive;
    font-size: 74px;
  }
  .card__contact {
    top: 576px;
    font-family: "Questrial", sans-serif;
    font-size: 26px;
    letter-spacing: 0.3px;
    word-spacing: 10px;
  }
</style>
</head>
<body>
  <main class="card">
    <aside class="card__panel">
      <svg class="card__emblem" width="200" height="370" viewBox="0 0 200 370">
        <defs>
          <radialGradient id="mic-tone" cx="50%" cy="45%" r="55%">
            <stop offset="0%" stop-color="#8cc81c"/>
            <stop offset="100%" stop-color="#b9e07a"/>
          </radialGradient>
        </defs>
        <ellipse cx="100" cy="185" rx="97" ry="182" fill="var(--card-white)" stroke="var(--ink)" stroke-width="2"/>
        <rect x="35" y="80" width="130" height="282" rx="60" fill="url(#mic-tone)"
              role="img" aria-label="Illustration of a vintage studio microphone in green"/>
      </svg>
    </aside>

    <section class="card__content">
      <h1 class="card__line card__title">~Stretch Every Idea~</h1>
      <p class="card__line card__tagline">Award Winning Melodex Podcast</p>
      <p class="card__line card__invite"><span>YOU ARE INVITED TO LISTEN</span></p>
      <p class="card__line card__host">Dr. Marla Quenby</p>
      <p class="card__line card__contact">www.drmarlaquenby-example.com 555-018-7364</p>
    </section>
  </main>
</body>
</html>
```